Education related business need name card design

We need name card design for long term study agent.
Company name is Harbor Lantern.
We support clients to connect to the world.
Clients are Japanese family who has primary and secondary school students.

Company Logo is reflection of the globe and HL (Harbor Lantern).
Since business is related to education, we would like to show reliability and love to see the world map (atlas) in the name card.

Target Market(s)

late 30's to 50's parents of primary and secondary students who are enthusiastic for education. Secondary school management

Industry/Entity Type

Education

Contact Information for Business Card

Company name, Address, Official position, Name, Phone number, Mobile number, email address,

Font styles to use
Serif
Other font styles liked:
• Century Gothic(logo)

Requirements
Must have
• Since businee is related to education, we would like to show reliability and love to see the world map (atlas) in the name card.

```html
<!DOCTYPE html>
<html lang="en">
<head>
<meta charset="utf-8">
<title>Harbor Lantern — Business Card</title>
<link href="https://fonts.googleapis.com/css2?family=Arimo:wght@400;700&display=swap" rel="stylesheet">
<style>
  :root {
    --page: #d9d6d2;
    --card: #141414;
    --card-edge: #1d1d1d;
    --accent: #1a86d9;
    --ink: #ffffff;
    --muted: #b8b8b8;
    --divider: #5a5a5a;
  }
  * { box-sizing: border-box; margin: 0; padding: 0; }
  html, body {
    width: 1200px; height: 787px; overflow: hidden;
    background: var(--page);
    font-family: "Arimo", Arial, sans-serif;
  }
  .stage {
    position: relative; width: 1200px; height: 787px;
    display: flex; align-items: center; justify-content: center; gap: 50px;
  }
  .card {
    position: relative; width: 525px; height: 300px;
    background: var(--card);
    border: 1px solid var(--card-edge);
    box-shadow: 0 6px 18px rgba(0,0,0,.25);
  }
  /* Reverse side */
  .card--reverse {
    display: flex; flex-direction: column; align-items: center; justify-content: center;
  }
  .brand-mark {
    display: flex; align-items: center; gap: 14px;
    color: var(--muted); font-size: 30px; font-weight: 400;
  }
  .brand-mark__dot {
    width: 22px; height: 22px; border-radius: 50%; background: var(--muted);
  }
  .reverse-url {
    margin-top: 34px; color: var(--ink); font-size: 14px; letter-spacing: 3px;
  }
  /* Front side */
  .card--front { display: flex; align-items: center; }
  .front-brand {
    width: 270px; display: flex; flex-direction: column; align-items: center; gap: 14px;
    color: var(--accent); font-size: 15px;
  }
  .front-brand__dot {
    width: 56px; height: 56px; border-radius: 50%; background: var(--accent);
  }
  .front-divider {
    width: 1px; height: 210px; background: var(--divider);
  }
  .contact { padding-left: 22px; color: var(--ink); font-size: 15px; line-height: 1.35; }
  .contact__name { color: var(--accent); font-size: 20px; font-weight: 700; }
  .contact__title { color: var(--accent); font-size: 15px; margin-bottom: 10px; }
  .contact__row { display: flex; align-items: center; gap: 8px; }
  .contact__row svg { width: 13px; height: 13px; fill: var(--accent); flex: none; }
  .contact__plain { padding-left: 0; }
  .contact__indent { padding-left: 21px; }
</style>
</head>
<body>
<main class="stage">
  <section class="card card--reverse">
    <div class="brand-mark"><span class="brand-mark__dot"></span>Harbor Lantern</div>
    <p class="reverse-url">www.harborlantern.example</p>
  </section>

  <section class="card card--front">
    <div class="front-brand">
      <span class="front-brand__dot"></span>
      <span>Harbor Lantern Pte. Ltd.</span>
    </div>
    <div class="front-divider"></div>
    <div class="contact">
      <p class="contact__name">Kenji Mori</p>
      <p class="contact__title">President</p>
      <p class="contact__indent">2170 Alder Crest Road</p>
      <p class="contact__indent">Maple Bay, NY 10542</p>
      <p class="contact__row">
        <svg viewBox="0 0 16 16" aria-hidden="true"><path d="M3 1h3l1.5 4-2 1.2a9 9 0 0 0 4.3 4.3L11 8.5l4 1.5v3a2 2 0 0 1-2 2A13 13 0 0 1 1 3a2 2 0 0 1 2-2z"/></svg>
        555 0142 7731
      </p>
      <p class="contact__row">
        <svg viewBox="0 0 16 16" aria-hidden="true"><path d="M4 0h8a1 1 0 0 1 1 1v14a1 1 0 0 1-1 1H4a1 1 0 0 1-1-1V1a1 1 0 0 1 1-1zm1 2v10h6V2zm3 11a1 1 0 1 0 0 2 1 1 0 0 0 0-2z"/></svg>
        555 0198 4620
      </p>
      <p class="contact__row">
        <svg viewBox="0 0 16 16" aria-hidden="true"><path d="M0 3h16v10H0zm1.5 1.2L8 9l6.5-4.8V4h-13z"/></svg>
        kenji@harborlantern.example
      </p>
      <p class="contact__row">
        <svg viewBox="0 0 16 16" aria-hidden="true"><circle cx="8" cy="8" r="7.5"/></svg>
        www.harborlantern.example
      </p>
    </div>
  </section>
</main>
</body>
</html>
```